Briefpapier, Visitenkarten, Bindemappe, Brieumschläge....
Zielgruppe
Steuerberatung vorwiegen für Unternehmer
Aufgabenstellung
Ein Logo ist bereits vorhanden (siehe Analgen) kann aber gerne auch bei einer guten Idee modernisiert werden. Ganz ein neues Logo möchte ich meinen Kunden jedoch ersparen, da ich es erst von zwei Jahren gewechselt habe. Grundfarbe grün wie Pantone 2293 C.
Als Anhaltspunkt was derzeit bei im Einsatz ist, habe ich die entsprechenden Dateien hochgeladen.

```html
<!DOCTYPE html>
<html lang="de">
<head>
<meta charset="utf-8">
<title>Briefumschlag – Steuerberater Konrad Wehlau</title>
<link rel="stylesheet" href="https://fonts.googleapis.com/css2?family=Roboto:wght@300;400;700&display=swap">
<style>
  :root {
    --brand-green: #9bc53d;
    --contact-green: #b5d47a;
    --ink: #111111;
    --paper: #ffffff;
    --shadow: rgba(0, 0, 0, 0.35);
  }
  * { margin: 0; padding: 0; box-sizing: border-box; }
  html, body {
    width: 1200px;
    height: 597px;
    overflow: hidden;
    background: var(--paper);
  }
  .envelope {
    position: relative;
    width: 1200px;
    height: 597px;
    background: var(--paper);
    font-family: "Roboto", Arial, sans-serif;
    overflow: hidden;
  }
  .brand-band {
    position: absolute;
    left: 0;
    top: 377px;
    width: 1200px;
    height: 220px;
    background: var(--brand-green);
  }
  .sender {
    position: absolute;
    left: 105px;
    top: 65px;
  }
  .sender-mark {
    position: absolute;
    left: 0;
    top: 2px;
    width: 96px;
    height: 96px;
    background: var(--brand-green);
  }
  .sender-name {
    position: absolute;
    left: 126px;
    top: 0;
    font-weight: 400;
    font-size: 46px;
    line-height: 54px;
    color: var(--ink);
    white-space: nowrap;
  }
  .sender-contact {
    position: absolute;
    left: 126px;
    top: 120px;
    font-weight: 300;
    font-size: 16.5px;
    line-height: 26px;
    color: var(--contact-green);
    white-space: nowrap;
  }
  .address-window {
    position: absolute;
    left: 105px;
    top: 283px;
    width: 473px;
    height: 291px;
    background: var(--paper);
    border: 1.5px solid var(--ink);
  }
  .claim {
    position: absolute;
    left: 627px;
    top: 442px;
    width: 490px;
    height: 107px;
    background: var(--paper);
    box-shadow: 8px 8px 6px var(--shadow);
    padding: 19px 0 0 14px;
  }
  .claim-line {
    display: block;
    font-weight: 700;
    font-size: 27px;
    line-height: 46px;
    letter-spacing: 0.6px;
    color: var(--ink);
    text-transform: uppercase;
    white-space: nowrap;
  }
</style>
</head>
<body>
  <div class="envelope">
    <div class="brand-band"></div>

    <div class="sender">
      <div class="sender-mark"></div>
      <div class="sender-name">Steuerberater<br>Konrad Wehlau</div>
      <div class="sender-contact">
        Lindenweg 4, 86150 Kerbach<br>
        www.kanzlei-wehlau.de, post@kanzlei-wehlau.de
      </div>
    </div>

    <div class="address-window"></div>

    <div class="claim">
      <span class="claim-line">Ergebnisorientiert denken,</span>
      <span class="claim-line">Persönlich handeln.</span>
    </div>
  </div>
</body>
</html>
```